Product Packaging Design for Luxury Make Up Brush Set-Minimal, Elegant, Chic

I need the packaging designed for new company, VÉLA, based in the United Kingdom. I have not developed the entire brand campaign yet, but I have a logo as attached. We are trying to emulate the 'feel' of RIV, Lumette, or Kirelo (https://www.kirelo-shop.example/) type of luxe style.
This is for a new brand of luxury and chic makeup brushes (and cosmetics organisers) called VÉLA. These are intelligently designed professional make up brushes that are designed to reflect a timeless elegance that incorporates chic trends in colours and materials. The cosmetic organizers and makeup brushes are European Chic; always stylish and intelligently designed. VÉLA in when form meets function in luxury cosmetics. What I am looking for now is packaging is for a 12-piece luxe makeup brush set. I have attached pictures of the set and a 'mood board' document with some images and fonts as well as the packaging diecut. Looking forward to discussing the details with the right designer. Thanks, Tova x
Updates

I have found a stock photo that has a very editorial feel and incorporates the neutral tones I like. I would like to see her on the front of the box. I have attached the image. Hope that fits into what you were planning. Thanks,Tova Added Friday, December 12, 2014

Target Market(s)

women, teenagers, make up artists and aficionados, those buying a gift for target market.

Industry/Entity Type

It Company

Font styles to use
Serif
Sans Serif
Script

Colors
000000
ffffff
757575
ceeae6
fff5ee
fee3d4
1b1b1b
e24096

Requirements
Must have
• I have attached another document titled 'make up brush descriptions' that has the details for the sales copy that needs to be on the packaging. Pictures of the set or at least a few brushes.
Nice to have
• I am not dead set on the colours I chose but I think less is more, classic black-white-neutral tones with perhaps a colour pop (like the dark pink/red I added). The brushes have rose-gold ferrules which should be shown in a pic(s) somewhere.
Should not have
• It should not look like the Belmi Professional box, I just uploaded it for some of the sales copy but have removed the photo as I wanted something original according to my brief. Also uploading a marketing image that is a great use of colours. That stock photo can be used in addition to the other if you see fit as well.
• Thanks, Tova

```html
<!DOCTYPE html>
<html lang="en">
<head>
<meta charset="utf-8">
<title>VÉLA Professional Brush Set – Packaging Panels</title>
<link rel="stylesheet" href="https://fonts.googleapis.com/css2?family=EB+Garamond:wght@400;500&family=Pinyon+Script&display=swap">
<style>
  :root{
    --black:#000000;
    --ink:#1b1b1b;
    --white:#ffffff;
    --grey:#757575;
    --stage:#a9a9a9;
    --pink:#e24096;
    --blush:#fee3d4;
    --shell:#fff5ee;
    --mint:#ceeae6;
    --serif:"EB Garamond", Garamond, Georgia, serif;
    --script:"Pinyon Script", cursive;
  }
  *{box-sizing:border-box;margin:0;padding:0}
  html,body{width:1200px;height:960px;overflow:hidden}
  body{background:var(--stage);font-family:var(--serif);color:var(--white);position:relative}

  .dieline{position:absolute;left:70px;top:70px;display:flex;gap:20px}
  .panel{position:relative;height:820px;background:var(--ink);overflow:hidden}
  .panel--side{width:200px}
  .panel--main{width:300px}
  .layer{position:absolute;left:0;top:0}

  .wordmark{font-family:var(--serif);font-weight:500;color:var(--white);text-align:center;letter-spacing:.02em;line-height:1}
  .tagline-small{font-size:7px;letter-spacing:.35em;text-align:center;color:var(--white)}
  .professional{font-family:var(--serif);color:var(--pink);text-align:center;line-height:1}
  .brush-set{font-family:var(--script);color:var(--white);text-align:center;line-height:1}

  /* front */
  .front-photo{position:absolute;left:0;top:0;width:300px;height:330px;
    background:radial-gradient(ellipse 55% 60% at 50% 38%, #e7c2ad 0%, #c98f78 45%, #f4ece8 78%, #ffffff 100%)}
  .front-brand{position:absolute;left:0;top:400px;width:300px}
  .front-brand .wordmark{font-size:66px}
  .front-brand .tagline-small{margin-top:6px}
  .front-brand .professional{font-size:25px;margin-top:44px}
  .front-brand .brush-set{font-size:46px;margin-top:0}
  .front-copy{position:absolute;left:30px;top:640px;width:240px;text-align:center;font-size:16px;line-height:1.3}
  .offer{position:absolute;left:8px;bottom:8px;font-size:13px;line-height:1.15;color:var(--white)}

  /* side A */
  .sideA-photo{position:absolute;left:0;width:200px}
  .sideA-photo--top{top:0;height:180px;background:linear-gradient(160deg,#ffffff 20%,#f1e2d4 55%,#caa27e 100%)}
  .sideA-photo--cups{top:215px;height:170px;background:linear-gradient(180deg,#f6f6f6,#bdbdbd 60%,#2a2a2a)}
  .sideA-photo--case{top:395px;height:170px;background:linear-gradient(180deg,#eeeeee,#a6a6a6 55%,#1e1e1e)}
  .sideA-brand{position:absolute;left:0;top:590px;width:200px}
  .sideA-brand .wordmark{font-size:34px}
  .sideA-brand .professional{font-size:14px;margin-top:10px}
  .sideA-brand .brush-set{font-size:24px}
  .contact{position:absolute;left:20px;top:710px;width:160px;font-size:9.5px;line-height:1.35;text-align:center;color:var(--white)}

  /* side B: brush guide */
  .guide{position:absolute;left:10px;top:14px;width:180px}
  .guide-intro{font-size:9.5px;line-height:1.25;color:var(--pink);margin-bottom:8px}
  .brush-list{list-style:none}
  .brush{margin-bottom:5px}
  .brush-name{display:block;background:var(--grey);color:var(--white);font-size:8.5px;padding:1px 4px;width:72%;
    clip-path:polygon(0 0,92% 0,100% 100%,0 100%)}
  .brush-use{font-size:8.3px;line-height:1.22;color:var(--white);margin-top:2px;border-bottom:1px solid #3a3a3a;padding-bottom:3px}
  .brush--pod .brush-name{background:var(--pink)}

  /* back */
  .back-photo{position:absolute;left:0;top:0;width:300px;height:300px;
    background:radial-gradient(ellipse 40% 30% at 25% 22%, #d9c8b4 0%, transparent 70%),
               radial-gradient(ellipse 30% 55% at 60% 55%, rgba(226,64,150,.55) 0%, transparent 70%),
               radial-gradient(ellipse 25% 25% at 45% 20%, #3a3ea8 0%, transparent 70%),
               var(--black)}
  .back-brand{position:absolute;left:0;top:315px;width:300px}
  .back-brand .wordmark{font-size:44px}
  .back-brand .professional{font-size:18px;margin-top:14px}
  .back-brand .brush-set{font-size:32px}
  .spec{position:absolute;left:24px;width:250px}
  .spec-title{font-size:13px;color:var(--pink);border-bottom:1px solid var(--grey);padding-bottom:1px;margin-bottom:3px}
  .spec--materials{top:490px}
  .spec--materials ul{list-style:none;font-size:13px;line-height:1.25;padding-left:14px}
  .spec--materials li{position:relative}
  .spec--materials li::before{content:"";position:absolute;left:-12px;top:7px;width:5px;height:5px;border-radius:50%;background:var(--white)}
  .spec--animal{top:600px}
  .spec--animal p{font-size:13px;line-height:1.2}
  .back-lineup{position:absolute;left:0;top:640px;width:300px;height:180px;background:var(--white)}
  .lineup-photo{position:absolute;left:30px;top:665px;width:240px;height:140px;
    background:linear-gradient(180deg,#d7d7d7 0%,#b98a6e 22%,#2b2b2b 30%,#1b1b1b 100%)}
</style>
</head>
<body>
<main class="dieline">

  <!-- side panel: product views and contact -->
  <section class="panel panel--side">
    <div class="sideA-photo sideA-photo--top" role="img" aria-label="Powder brush with loose powder dusting off the bristles"></div>
    <div class="sideA-photo sideA-photo--cups" role="img" aria-label="Brush set standing in its leather cylinder case"></div>
    <div class="sideA-photo sideA-photo--case" role="img" aria-label="Brushes fanned out of the open storage case"></div>
    <svg class="layer" width="200" height="820" viewBox="0 0 200 820" aria-hidden="true">
      <polygon points="0,150 200,225 200,237 0,162" fill="var(--pink)"/>
      <polygon points="0,180 200,255 200,215 0,215" fill="var(--ink)" opacity="0"/>
      <polygon points="0,368 200,398 200,404 0,374" fill="var(--pink)"/>
      <polygon points="0,548 200,578 200,584 0,554" fill="var(--pink)"/>
    </svg>
    <div class="sideA-brand">
      <div class="wordmark">VÉLA</div>
      <div class="professional">Professional</div>
      <div class="brush-set">Brush Set</div>
    </div>
    <p class="contact">Your Address Here…<br>Contact No. Here<br>E-Mail: hello@vela.example<br>Visit us on: www.vela.example</p>
  </section>

  <!-- front panel -->
  <section class="panel panel--main">
    <div class="front-photo" role="img" aria-label="Editorial beauty photograph of a model applying blush with a large brush"></div>
    <svg class="layer" width="300" height="820" viewBox="0 0 300 820" aria-hidden="true">
      <polygon points="0,300 300,360 300,420 0,420" fill="var(--ink)"/>
      <polygon points="0,300 300,360 300,372 0,312" fill="var(--pink)"/>
      <polygon points="0,312 300,372 300,420 0,420" fill="var(--ink)"/>
      <polygon points="200,760 300,738 300,820 200,820" fill="var(--white)"/>
      <polygon points="0,780 300,720 300,730 0,790" fill="none"/>
      <polygon points="0,768 230,802 230,820 0,820" fill="var(--pink)"/>
    </svg>
    <div class="front-brand">
      <div class="wordmark">VÉLA</div>
      <div class="tagline-small">COSMETICS · LONDON</div>
      <div class="professional">Professional</div>
      <div class="brush-set">Brush Set</div>
    </div>
    <p class="front-copy">The ultimate make up brush set complete with 12 must have make up brushes with deluxe storage case!</p>
    <p class="offer">With Free<br>Silicon Cleaning Pod</p>
  </section>

  <!-- side panel: brush guide -->
  <section class="panel panel--side">
    <div class="guide">
      <p class="guide-intro">Our ultimate brush set is all you need to complete your beauty tool kit. Each of our 12 brushes have been selected by VÉLA as tools to create your perfection.</p>
      <ol class="brush-list">
        <li class="brush"><span class="brush-name">1. Eyeliner Brush</span><p class="brush-use">Create smooth and even lines. Use with gel or liquid liners.</p></li>
        <li class="brush"><span class="brush-name">2. Short Shadow Brush</span><p class="brush-use">Concentrated colour application. Apply colour onto small areas of the eye, such as the outer eyelid.</p></li>
        <li class="brush"><span class="brush-name">3. Eye Shadow Brush</span><p class="brush-use">Even application of colour. Place colour across the whole lid for an even and strong finish.</p></li>
        <li class="brush"><span class="brush-name">4. Blending Brush</span><p class="brush-use">Controlled blending. Blend colours together across the lid for a soft, diffused effect.</p></li>
        <li class="brush"><span class="brush-name">5. Large Shadow Brush</span><p class="brush-use">Uniformly cover the whole lid with product. Apply cream shadow for quick and even coverage.</p></li>
        <li class="brush"><span class="brush-name">6. Dual Fibre Stippling Brush</span><p class="brush-use">Soft blush application. Creates a diffused finish with mineral or cream products.</p></li>
        <li class="brush"><span class="brush-name">7. Powder Brush</span><p class="brush-use">Precise placement of blush. Use for powder application.</p></li>
        <li class="brush"><span class="brush-name">8. Large Angled Contour</span><p class="brush-use">Cheek application. Use the angle to softly contour the cheekbone.</p></li>
        <li class="brush"><span class="brush-name">9. Foundation Brush</span><p class="brush-use">Smooth foundation application. Apply liquid or cream foundation evenly.</p></li>
        <li class="brush"><span class="brush-name">10. Angled Shading Brush</span><p class="brush-use">Soft application of colour. Use for brow highlighting and shading.</p></li>
        <li class="brush"><span class="brush-name">11. Angled Blending Brush</span><p class="brush-use">Create precise lining. Works with powder or cream to define.</p></li>
        <li class="brush"><span class="brush-name">12. Crease Brush</span><p class="brush-use">Soften and blend colour along the crease and lower lash line.</p></li>
        <li class="brush brush--pod"><span class="brush-name">Silicon Cleaning Pod</span><p class="brush-use">Gently scrub brushes over the ridges to lift makeup and build-up.</p></li>
      </ol>
    </div>
  </section>

  <!-- back panel -->
  <section class="panel panel--main">
    <div class="back-photo" role="img" aria-label="Two brushes releasing a cloud of pink and blue pigment on black"></div>
    <div class="back-brand">
      <div class="wordmark">VÉLA</div>
      <div class="professional">Professional</div>
      <div class="brush-set">Brush Set</div>
    </div>
    <div class="spec spec--materials">
      <h2 class="spec-title">Material for each brush</h2>
      <ul>
        <li>Aluminium ferrule</li>
        <li>Baking varnish wooden handle</li>
        <li>Synthetic hair.</li>
        <li>PU leather cosmetic cylinder.</li>
      </ul>
    </div>
    <div class="spec spec--animal">
      <h2 class="spec-title">Animal Friendly</h2>
      <p>All our brushes are made from soft synthetic hair.</p>
    </div>
    <div class="back-lineup"></div>
    <svg class="layer" width="300" height="820" viewBox="0 0 300 820" aria-hidden="true">
      <polygon points="0,640 300,690 300,640" fill="var(--ink)"/>
      <polygon points="0,640 300,690 300,700 0,650" fill="var(--pink)"/>
    </svg>
    <div class="lineup-photo" role="img" aria-label="Twelve black brushes with rose-gold ferrules laid in a row"></div>
  </section>

</main>
</body>
</html>
```